Looking for attractive banner design (print banner)

I am looking to redesign a banner to be more attractive and professional. This will be a print banner, 24" x 36" vertical. I am attaching the original concept to reference. High resolution file for print required. fading or blurring the background, attractive fonts, gradient highlight for text boxes, etc.

```html
<!DOCTYPE html>
<html lang="en">
<head>
<meta charset="utf-8">
<title>Essential Oils for the Horse &amp; Rider</title>
<link href="https://fonts.googleapis.com/css2?family=Montserrat:wght@800&family=Oswald:wght@500&family=PT+Sans+Narrow&display=swap" rel="stylesheet">
<style>
  :root {
    --gold: #f2cf45;
    --gold-dim: #c9a93a;
    --white: #ffffff;
    --band-dark: rgba(40, 34, 14, 0.72);
    --band-fade: rgba(40, 34, 14, 0);
    --footer: #5a3b22;
    --photo-top: #8a8a3a;
    --photo-mid: #6f7a34;
    --photo-low: #5b5a2e;
  }
  * { margin: 0; padding: 0; box-sizing: border-box; }
  html, body { width: 800px; height: 1200px; overflow: hidden; background: #333; }
  .banner {
    position: relative; width: 800px; height: 1200px; overflow: hidden;
    font-family: "PT Sans Narrow", sans-serif; color: var(--white);
  }
  .backdrop {
    position: absolute; inset: 0;
    background:
      radial-gradient(ellipse 40% 55% at 52% 55%, rgba(215, 205, 185, 0.55), rgba(215, 205, 185, 0) 70%),
      radial-gradient(ellipse 60% 30% at 50% 15%, rgba(200, 190, 80, 0.6), rgba(200, 190, 80, 0) 70%),
      linear-gradient(180deg, var(--photo-top) 0%, var(--photo-mid) 45%, var(--photo-low) 100%);
  }
  .frame {
    position: absolute; inset: 8px;
    border: 2px solid rgba(242, 207, 69, 0.55);
    pointer-events: none;
  }
  .title {
    position: absolute; left: 0; right: 0; top: 26px; text-align: center;
    font-family: "Montserrat", sans-serif; font-weight: 800; line-height: 1;
  }
  .title-main { display: block; font-size: 82px; color: var(--gold); }
  .title-sub { display: block; font-size: 55px; color: var(--white); margin-top: 10px; }
  .topic { position: absolute; padding: 4px 12px; width: 340px; white-space: nowrap; }
  .topic-left {
    left: 10px; text-align: left; padding-left: 28px;
    background: linear-gradient(90deg, var(--band-dark) 60%, var(--band-fade));
  }
  .topic-right {
    right: 10px; text-align: right; padding-right: 28px;
    background: linear-gradient(270deg, var(--band-dark) 60%, var(--band-fade));
  }
  .topic-name {
    display: inline-block; font-family: "Oswald", sans-serif; font-weight: 500;
    font-size: 27px; line-height: 26px; color: var(--gold);
    border-bottom: 2px solid var(--gold-dim); text-transform: uppercase;
  }
  .topic-oils { font-size: 25px; line-height: 25px; margin-top: 3px; }
  .footer {
    position: absolute; left: 8px; right: 8px; bottom: 8px; height: 56px;
    background: var(--footer); display: flex; align-items: center; justify-content: center;
    font-family: "Oswald", sans-serif; font-weight: 500; font-size: 27px; color: var(--gold);
  }
</style>
</head>
<body>
<main class="banner">
  <div class="backdrop" role="img" aria-label="Soft-focus photo of a woman in a white hat and red suspenders standing beside a grazing grey horse on a woodland path"></div>
  <div class="frame"></div>

  <h1 class="title">
    <span class="title-main">ESSENTIAL OILS</span>
    <span class="title-sub">FOR THE HORSE &amp; RIDER</span>
  </h1>

  <section class="topic topic-left" style="top:182px"><h2 class="topic-name">Brain</h2><p class="topic-oils">Grankincense, Mind Lift,<br>Clear Focus, Cedarwood</p></section>
  <section class="topic topic-left" style="top:290px"><h2 class="topic-name">Skin &amp; Hair</h2><p class="topic-oils">Cedarwood, Lavender,<br>Geranium, Frankincense, Myrrh</p></section>
  <section class="topic topic-left" style="top:390px"><h2 class="topic-name">Ears</h2><p class="topic-oils">Helichrysum, Clean Air,<br>Tea Tree, Juniper</p></section>
  <section class="topic topic-left" style="top:496px"><h2 class="topic-name">Lungs</h2><p class="topic-oils">Breathe Ease, Night Wing<br>Eucalyptus (all), Guardian,<br>Tea Tree, Blue Meadow</p></section>
  <section class="topic topic-left" style="top:627px"><h2 class="topic-name">Muscles</h2><p class="topic-oils">Calm Muscle,<br>Deep Soothe, Marjoram,<br>Cypress, Peppermint,<br>Highland Fir</p></section>
  <section class="topic topic-left" style="top:776px"><h2 class="topic-name">Immune Support</h2><p class="topic-oils">Guardian, Oregano,<br>Ocatea, Lifespan,<br>Lemon, Peppermint,<br>Cinnamon Bark, Rosemary</p></section>
  <section class="topic topic-left" style="top:920px"><h2 class="topic-name">Tendons<br>&amp; Ligaments</h2><p class="topic-oils">Palo Santo, Lemongrass,<br>Rosemary, Peppermint</p></section>
  <section class="topic topic-left" style="top:1042px"><h2 class="topic-name">Hoof (Horse)</h2><p class="topic-oils">Guardian, Tea Tree<br>Oregano, Frankincense</p></section>

  <section class="topic topic-right" style="top:184px"><h2 class="topic-name">Emotional<br>Support</h2><p class="topic-oils">Valiant, Solace, Summit Spirit,<br>Bright Heart, Lemon</p></section>
  <section class="topic topic-right" style="top:298px"><h2 class="topic-name">Eyes</h2><p class="topic-oils">Frankincense, Sandalwood,<br>Carrot Seed, Lemongrass</p></section>
  <section class="topic topic-right" style="top:412px"><h2 class="topic-name">Mouth</h2><p class="topic-oils">Clove, Ocatea, Tea Tree<br>Wintergreen, Guardian</p></section>
  <section class="topic topic-right" style="top:516px"><h2 class="topic-name">Heart</h2><p class="topic-oils">Orange,<br>Y,lang Ylang, Cypress,<br>Helichrysum, Palmarosa</p></section>
  <section class="topic topic-right" style="top:636px"><h2 class="topic-name">Digestion</h2><p class="topic-oils">Gut Calm, Easy Tummy,<br>Ginger,<br>Fennel, Peppermint,</p></section>
  <section class="topic topic-right" style="top:778px"><h2 class="topic-name">Hormonal<br>Balance</h2><p class="topic-oils">Clary Sage, Moon Cycle,<br>Gland Balance, Myrtle, Blue Meadow</p></section>
  <section class="topic topic-right" style="top:924px"><h2 class="topic-name">Bones &amp; Joints</h2><p class="topic-oils">Ache Fade, Helichrysum,<br>Wintergreen, Cool Blue, Valiant</p></section>
  <section class="topic topic-right" style="top:1032px"><h2 class="topic-name">Feet (Rider)</h2><p class="topic-oils">Earth Root, Valiant, Guardian,<br>Clean Air, Oregano</p></section>

  <footer class="footer">DISCLAIMER: NOT EVALUATED BY THE FDA, NOT MEDICAL ADVICE.</footer>
</main>
</body>
</html>
```